Powepoint template for an investment group

Need high end clear clean concise creative luxurious

Have royal clients
High end/billionaire investors

Using ross gold logo can be creative
Must habe page numbers
Logo preference header top right
Page number footer bottom right

The first page of the ppt maybe a big block of dark grey and oberi investment group written on the front page in rose gold

Target Market(s)

Investors at a high level

Requirements
Must have
• Luxury feel

```html
<!DOCTYPE html>
<html lang="en">
<head>
<meta charset="utf-8">
<title>Oberi Investment Group – Company Presentation 2022</title>
<link href="https://fonts.googleapis.com/css2?family=Montserrat:wght@300;400;600;700&family=Tinos:wght@400;700&display=swap" rel="stylesheet">
<style>
:root{
  --rose:#e8b4ac;
  --rose-soft:#f3d6d1;
  --graphite:#58585a;
  --ink:#4a4a4c;
  --text:#6b6b6d;
  --paper:#ffffff;
  --mist:#f1f1f2;
  --backdrop:#1f1f1f;
}
*{margin:0;padding:0;box-sizing:border-box}
html,body{width:1065px;height:1200px;overflow:hidden;background:var(--backdrop)}
body{position:relative;font-family:"Montserrat",sans-serif;color:var(--text)}
.slide{position:absolute;background:var(--paper);overflow:hidden}
.slide-sm{width:288px;height:162px}
.abs{position:absolute}
.placeholder{position:absolute}
/* brand mark */
.brand{position:absolute;text-align:center;color:var(--rose);font-family:"Montserrat",sans-serif;font-weight:300;line-height:1;white-space:nowrap}
.brand .name{display:block;letter-spacing:.28em}
.brand .sub{display:block;letter-spacing:.12em}
.slide-sm .brand{right:8px;top:12px;width:62px}
.slide-sm .brand .name{font-size:10px;padding-left:.28em}
.slide-sm .brand .sub{font-size:3px;margin-top:2px;opacity:.7}
.footer-line{position:absolute;left:0;right:18px;top:150px;height:1px;background:var(--rose)}
.page-no{position:absolute;right:9px;top:147px;font-size:5px;color:var(--rose);font-weight:600}
.h-rose{color:var(--rose);font-weight:700;line-height:1.05}
.h-light{color:var(--rose);font-weight:400;line-height:1.05}
.copy{font-family:Arial,"Montserrat",sans-serif;font-size:3.2px;line-height:1.35;color:var(--text)}
/* cover */
.cover{left:85px;top:77px;width:895px;height:503px}
.cover .brand{left:625px;top:50px;width:240px}
.cover .brand .name{font-size:50px;letter-spacing:.24em;padding-left:.24em}
.cover .brand .sub{font-size:15px;margin-top:14px;color:#d9a9a1}
.cover-band{position:absolute;left:285px;top:153px;width:566px;height:66px;background:var(--graphite);display:flex;align-items:center;justify-content:center}
.cover-band h1{font-size:35.5px;font-weight:700;color:var(--rose);letter-spacing:.01em;white-space:nowrap}
.cover-company{position:absolute;left:397px;top:222px;font-family:"Tinos",serif;font-size:46px;color:var(--graphite)}
.cover-presentation{position:absolute;left:397px;top:280px;font-family:"Tinos",serif;font-weight:700;font-size:58px;color:var(--rose)}
.cover-year{position:absolute;left:395px;top:341px;font-size:60px;font-weight:700;color:var(--graphite)}
.cover-rule{position:absolute;left:397px;top:419px;width:164px;height:3px;background:var(--rose)}
.cover-url{position:absolute;left:397px;top:442px;font-size:16px;letter-spacing:.42em;color:var(--ink);white-space:nowrap}
.cover-url span{color:var(--rose)}
/* contents */
.toc-item{position:absolute;width:118px}
.toc-item b{display:block;color:var(--rose);font-size:5.6px;font-weight:600;margin-bottom:2px}
.toc-item b i{font-style:normal;margin-right:4px}
/* check list */
.checks{position:absolute;left:140px;top:75px;list-style:none}
.checks li{font-family:Arial,sans-serif;font-size:3.8px;color:var(--text);height:10.2px}
.checks li::before{content:"✓";color:var(--rose);margin-right:5px}
.phone{position:absolute;border:1.2px solid #222;border-radius:3px;background:var(--paper);padding:9px 3px 3px}
.phone .p-title{font-size:3.6px;color:var(--rose);line-height:1.2}
.phone .p-icon{width:5px;height:5px;border:.6px solid var(--rose);margin:5px auto}
.phone .p-copy{font-size:2px;line-height:1.3;color:var(--text)}
.member{position:absolute;left:20px;width:110px;height:26px}
.member .avatar{position:absolute;left:14px;top:0;width:13px;height:13px;border-radius:50%;background:#d8cfcc}
.member .m-name{position:absolute;left:0;top:15px;width:42px;text-align:center;font-size:2.6px;color:var(--rose)}
.member .m-title{position:absolute;left:40px;top:0;font-size:4px;color:var(--ink)}
.member .copy{position:absolute;left:40px;top:5px;width:48px;font-size:2.1px}
.thanks .brand{left:12px;top:22px;width:112px;right:auto}
.thanks .brand .name{font-size:21px;letter-spacing:.24em;padding-left:.24em}
.thanks .brand .sub{font-size:6.5px;margin-top:6px}
.contact{position:absolute;left:0;top:105px;width:147px;height:30px;background:var(--graphite);padding:3px 0 0 17px;z-index:2}
.contact p{font-size:5px;color:#fff;line-height:1.55}
.contact p::before{content:"";display:inline-block;width:2.5px;height:2.5px;border-radius:50%;background:var(--rose);margin-right:2px;vertical-align:middle}
</style>
</head>
<body>

<!-- Cover -->
<section class="slide cover">
  <div class="placeholder" role="img" aria-label="3D figure relaxing on stacks of gold coins" style="left:56px;top:95px;width:323px;height:392px;background:radial-gradient(ellipse at 50% 55%,#cbb88a 0%,#e4dbc5 45%,#ffffff 75%)"></div>
  <div class="brand"><span class="name">OBERI</span><span class="sub">Investment Group</span></div>
  <div class="cover-band"><h1>OBERI INVESTMENT GROUP</h1></div>
  <div class="cover-company">Company</div>
  <div class="cover-presentation">Presentation</div>
  <div class="cover-year">2022</div>
  <div class="cover-rule"></div>
  <div class="cover-url">www.<span>oberiinvestmentgroup</span>.com</div>
</section>

<!-- 02 Contents -->
<section class="slide slide-sm" style="left:85px;top:598px">
  <div class="brand"><span class="name">OBERI</span><span class="sub">Investment Group</span></div>
  <div class="abs h-rose" style="left:22px;top:21px;font-size:15px">Contents</div>
  <div class="abs" style="left:22px;top:38px;width:70px;height:1.5px;background:var(--rose)"></div>
  <div class="toc-item" style="left:22px;top:53px"><b><i>1.</i>Lorem ipsum</b><p class="copy">Lorem ipsum dolor sit amet, consectetuer adipiscing elit, sed diam nonummy nibh euismod tincid</p></div>
  <div class="toc-item" style="left:22px;top:85px"><b><i>2.</i>Lorem ipsum</b><p class="copy">Lorem ipsum dolor sit amet, consectetuer adipiscing elit, sed diam nonummy nibh euismod tincid</p></div>
  <div class="toc-item" style="left:22px;top:114px"><b><i>3.</i>Lorem ipsum</b><p class="copy">Lorem ipsum dolor sit amet, consectetuer adipiscing elit, sed diam nonummy nibh euismod tincid</p></div>
  <div class="toc-item" style="left:154px;top:53px"><b><i>4.</i>Lorem ipsum</b><p class="copy">Lorem ipsum dolor sit amet, consectetuer adipiscing elit, sed diam nonummy nibh euismod tincid</p></div>
  <div class="toc-item" style="left:154px;top:85px"><b><i>5.</i>Lorem ipsum</b><p class="copy">Lorem ipsum dolor sit amet, consectetuer adipiscing elit, sed diam nonummy nibh euismod tincid</p></div>
  <div class="toc-item" style="left:154px;top:114px"><b><i>6.</i>Lorem ipsum</b><p class="copy">Lorem ipsum dolor sit amet, consectetuer adipiscing elit, sed diam nonummy nibh euismod tincid</p></div>
  <div class="footer-line"></div><div class="page-no">02</div>
</section>

<!-- 03 Functionality -->
<section class="slide slide-sm" style="left:389px;top:598px">
  <div class="brand"><span class="name">OBERI</span><span class="sub">Investment Group</span></div>
  <div class="abs h-rose" style="left:13px;top:25px;font-size:10px">FUNCTIONALITY</div>
  <div class="abs" style="left:13px;top:36px;width:88px;height:1px;background:var(--rose)"></div>
  <div class="abs copy" style="left:13px;top:44px;width:105px">
    <p>Lorem ipsum dolor sit amet, consectetuer adipiscing elit, sed diam nonummy nibh euismod tincidunt ut laoreet dolore magna aliquam erat volutpat. Ut wisi enim ad minim veniam, quis nostrud exerci tation ullamcorper suscipit lobortis nisl ut aliquip ex ea commodo consequat.</p><br>
    <p>Lorem ipsum dolor sit amet, consectetuer adipiscing elit, sed diam nonummy nibh euismod tincidunt ut laoreet dolore magna aliquam erat volutpat. Ut wisi enim ad minim veniam, quis nostrud exerci tation ullamc</p><br>
    <p>Lorem ipsum dolor sit amet, consectetuer adipiscing elit, sed diam nonummy nibh euismod tincidunt ut laoreet dolore magna aliquam erat volutpat. Ut wisi enim ad minim veniam.</p>
  </div>
  <svg class="abs" style="left:120px;top:40px" width="160" height="100" viewBox="120 40 160 100">
    <g stroke="var(--graphite)" stroke-width="1.2">
      <line x1="201" y1="95" x2="185" y2="61"/><line x1="201" y1="95" x2="215" y2="61"/>
      <line x1="201" y1="95" x2="164" y2="82"/><line x1="201" y1="95" x2="236" y2="82"/>
    </g>
    <circle cx="201" cy="95" r="17" fill="var(--graphite)"/>
    <circle cx="201" cy="95" r="11" fill="none" stroke="#fff" stroke-width=".8" stroke-dasharray="2 1.5"/>
    <text x="201" y="96.5" font-size="3.5" fill="#fff" text-anchor="middle" font-family="Montserrat,sans-serif" letter-spacing=".5">OBERI</text>
    <g fill="var(--graphite)"><circle cx="185" cy="61" r="11"/><circle cx="215" cy="61" r="11"/><circle cx="164" cy="82" r="11"/><circle cx="236" cy="82" r="11"/></g>
    <g fill="#fff" font-size="2.8" font-family="Montserrat,sans-serif" text-anchor="middle" font-weight="600">
      <text x="185" y="67">Option B</text><text x="215" y="67">Option C</text><text x="164" y="88">Option A</text><text x="236" y="88">Option D</text>
    </g>
    <g fill="none" stroke="#fff" stroke-width=".7"><circle cx="185" cy="57" r="2"/><rect x="213" y="55" width="4" height="4"/><rect x="162" y="77" width="4" height="3"/><rect x="234" y="77" width="4" height="3"/></g>
    <g font-size="2.6" font-family="Montserrat,sans-serif" fill="var(--rose)">
      <text x="154" y="52">Your Title</text><text x="230" y="50">Your Title</text><text x="133" y="79">Your Title</text><text x="251" y="79">Your Title</text>
    </g>
    <g font-size="1.8" font-family="Arial,sans-serif" fill="var(--text)">
      <text x="146" y="56">Short note on this point</text><text x="230" y="54">Short note on this point</text><text x="126" y="83">Short note on this point</text><text x="251" y="83">Short note on this point</text>
    </g>
    <circle cx="133" cy="127" r="5" fill="var(--rose)"/><circle cx="216" cy="127" r="5" fill="var(--rose)"/>
    <text x="133" y="128.5" font-size="4" fill="#fff" text-anchor="middle">£</text><text x="216" y="128.5" font-size="4" fill="#fff" text-anchor="middle">$</text>
    <g font-size="2.8" font-family="Montserrat,sans-serif" fill="var(--rose)" font-weight="600"><text x="140" y="124">LOREM IPSUM</text><text x="223" y="124">LOREM IPSUM</text></g>
    <g font-size="1.9" font-family="Arial,sans-serif" fill="var(--text)"><text x="140" y="128">Lorem ipsum dolor sit amet, consectetuer</text><text x="140" y="131">adipiscing elit, sed diam nonummy nibh</text><text x="223" y="128">Lorem ipsum dolor sit amet, consectetuer</text><text x="223" y="131">adipiscing elit, sed diam nonummy nibh</text></g>
  </svg>
  <div class="footer-line"></div><div class="page-no">03</div>
</section>

<!-- 04 Company advantage -->
<section class="slide slide-sm" style="left:692px;top:598px">
  <div class="brand"><span class="name">OBERI</span><span class="sub">Investment Group</span></div>
  <div class="abs" style="left:22px;top:31px;width:103px;height:100px;border:1px solid var(--rose)"></div>
  <div class="placeholder" role="img" aria-label="Photo of smiling colleagues working at a laptop" style="left:25px;top:34px;width:97px;height:94px;background:linear-gradient(135deg,#c9d6e2,#8fa3b8 55%,#d8c2b4)"></div>
  <div class="abs h-light" style="left:140px;top:30px;font-size:11px">COMPANY<br><b style="font-weight:600">ADVANTAGE</b></div>
  <div class="abs" style="left:140px;top:54px;width:71px;height:1.2px;background:var(--rose)"></div>
  <div class="abs copy" style="left:140px;top:62px;width:124px">
    <p>Lorem ipsum dolor sit amet, consectetuer adipiscing elit, sed diam nonummy nibh euismod tincidunt ut laoreet dolore magna aliquam erat volutpat. Ut wisi enim ad minim veniam, quis nostrud exerci tation ullam</p><br>
    <p>Lorem ipsum dolor sit amet, consectetuer adipiscing elit, sed diam nonummy nibh euismod tincidunt ut laoreet dolore magna aliquam erat volutpat. Ut wisi enim ad minim veniam, quis nostrud exerci tation ullam</p><br>
    <p>Lorem ipsum dolor sit amet, consectetuer adipiscing elit, sed diam nonummy nibh euismod tincidunt ut laoreet dolore magna aliquam erat volutpat. Ut wisi enim ad minim veniam, quis nostrud exerci</p>
  </div>
  <div class="footer-line"></div><div class="page-no">04</div>
</section>

<!-- 05 Market opportunities -->
<section class="slide slide-sm" style="left:85px;top:779px">
  <div class="brand"><span class="name">OBERI</span><span class="sub">Investment Group</span></div>
  <div class="abs h-light" style="left:15px;top:23px;font-size:10px">MARKET<br><b style="font-weight:600">OPPORTUNITIES</b></div>
  <div class="abs copy" style="left:15px;top:53px;width:260px">
    <p>Lorem ipsum dolor sit amet, consectetuer adipiscing elit, sed diam nonummy nibh euismod tincidunt ut laoreet dolore magna aliquam erat volutpat. Ut wisi enim ad minim veniam, quis nostrud exerci tation ullamcorper suscipit lobortis nisl ut aliquip ex ea commodo consequat. Duis autem vel eum iriure dolor in hendrerit i</p>
    <p style="margin-top:3px">Lorem ipsum dolor sit amet, consectetuer adipiscing elit, sed diam nonummy nibh euismod tincidunt ut laoreet dolore magna aliquam erat volutpat. Ut wisi enim ad minim veniam, quis nostrud exerci tation ullamcorper suscipit lobortis nisl ut aliquip ex ea commodo consequat. Duis autem vel eum iriure dolor in hendrerit in</p>
  </div>
  <svg class="abs" style="left:25px;top:88px" width="125" height="50" viewBox="0 0 125 50">
    <g font-size="2.2" fill="var(--text)" font-family="Arial,sans-serif"><text x="0" y="3">1000</text><text x="0" y="12">700</text><text x="0" y="21">500</text><text x="0" y="30">300</text><text x="0" y="39">100</text><text x="0" y="48">0</text></g>
    <path d="M12 47 C16 40 18 35 22 37 C26 39 27 46 31 44 C35 40 37 34 41 35 C45 37 45 43 49 41 C53 38 52 36 56 33 C60 30 62 20 66 20 C70 20 72 33 77 37 C82 42 86 42 90 47 Z" fill="var(--rose)"/>
    <g font-size="2.6" fill="var(--rose)" font-family="Arial,sans-serif"><text x="15" y="33">100</text><text x="26" y="43">20</text><text x="34" y="26">215</text><text x="47" y="33">135</text><text x="64" y="17">650</text><text x="80" y="38">80</text></g>
  </svg>
  <svg class="abs" style="left:153px;top:80px" width="100" height="58" viewBox="0 0 100 58">
    <g stroke="#f0d2cd" stroke-width=".4">
      <line x1="5" y1="6" x2="95" y2="6"/><line x1="5" y1="15" x2="95" y2="15"/><line x1="5" y1="24" x2="95" y2="24"/><line x1="5" y1="33" x2="95" y2="33"/><line x1="5" y1="42" x2="95" y2="42"/>
      <line x1="15" y1="2" x2="15" y2="51"/><line x1="30" y1="2" x2="30" y2="51"/><line x1="45" y1="2" x2="45" y2="51"/><line x1="60" y1="2" x2="60" y2="51"/><line x1="75" y1="2" x2="75" y2="51"/><line x1="90" y1="2" x2="90" y2="51"/>
    </g>
    <line x1="5" y1="51" x2="95" y2="51" stroke="var(--text)" stroke-width=".4"/>
    <rect x="38" y="2" width="18" height="4" fill="var(--rose)"/><text x="47" y="5" font-size="2.3" fill="#fff" text-anchor="middle" font-family="Arial,sans-serif">TEXT HERE</text>
    <g fill="none" stroke-width=".8">
      <path d="M5 50 C15 25 25 18 40 16 C55 14 60 12 75 20 C85 25 88 15 92 11" stroke="var(--rose)"/>
      <path d="M5 50 C15 30 25 26 40 25 C55 24 65 25 75 28 C85 30 90 22 92 20" stroke="var(--graphite)"/>
      <path d="M5 50 C15 35 25 32 40 31 C55 30 65 38 75 41 C85 44 90 36 92 35" stroke="var(--rose)"/>
      <path d="M5 50 C15 40 25 38 40 38 C55 38 65 42 75 45 C85 45 90 40 92 38" stroke="var(--graphite)"/>
    </g>
  </svg>
  <div class="footer-line"></div><div class="page-no">05</div>
</section>

<!-- 06 Domain -->
<section class="slide slide-sm" style="left:389px;top:779px">
  <div class="placeholder" role="img" aria-label="Faded background photo of a desk with charts" style="left:0;top:0;width:288px;height:162px;background:linear-gradient(90deg,#e6e8ea,#f6f6f7 60%,#ffffff)"></div>
  <div class="brand"><span class="name">OBERI</span><span class="sub">Investment Group</span></div>
  <svg class="abs" style="left:28px;top:36px" width="102" height="100" viewBox="0 0 102 100"><g fill="none" stroke="var(--rose)" stroke-width="1.5"><path d="M0 10 V1 H9"/><path d="M101 89 V98 H92"/></g></svg>
  <div class="placeholder" role="img" aria-label="Photo of hands typing on a keyboard with financial charts overlay" style="left:33px;top:39px;width:90px;height:92px;background:linear-gradient(160deg,#9fb4cc,#3f5f86 55%,#1f3554)"></div>
  <div class="abs h-light" style="left:140px;top:37px;font-size:7px">WHAT'S A DOMAIN?<br>IT'S THAT NAME UP<br><b style="font-weight:600">IN THE ADDRESS BAR.</b></div>
  <ul class="checks" style="top:76px">
    <li>Fits your business or products and remember</li>
    <li>Is easy to spell and rememberor products</li>
    <li>Fits your business or products and remember</li>
    <li>Is easy to spell and remember easy to spell</li>
    <li>Fits your business or products spell and rememberor</li>
    <li>Is easy to spell and remember business or products</li>
  </ul>
  <div class="footer-line"></div><div class="page-no">06</div>
</section>

<!-- 07 Our company -->
<section class="slide slide-sm" style="left:692px;top:779px">
  <div class="brand"><span class="name">OBERI</span><span class="sub">Investment Group</span></div>
  <div class="abs" style="left:0;top:36px;width:95px;height:99px;background:var(--rose)"></div>
  <div class="placeholder" role="img" aria-label="Laptop showing a team meeting illustration" style="left:21px;top:50px;width:130px;height:71px;background:linear-gradient(180deg,#2b2b2d 0 6%,#f4f4f4 6% 82%,#b9b9bb 82%)"></div>
  <div class="abs h-rose" style="left:160px;top:37px;font-size:8.5px">OUR COMPANY<br>IPSUM SIT</div>
  <div class="abs" style="left:160px;top:61px;width:76px;height:1.2px;background:var(--rose)"></div>
  <div class="abs copy" style="left:160px;top:66px;width:118px">
    <p>Lorem ipsum dolor sit amet, consectetuer adipiscing elit, sed diam nonummy nibh euismod tincidunt ut laoreet dolore magna aliquam erat volutpat. Ut wisi enim ad minim veniam, quis nostrud exerci tation ullamcorper suscipit lobortis nisl ut aliquip ex ea commodo consequat. Duis autem vel eum iriure dolor in hendrerit</p><br>
    <p>Lorem ipsum dolor sit amet, consectetuer adipiscing elit, sed diam nonummy nibh</p><br>
    <p>m ipsum dolor sit amet, consectetuer adipiscing elit, sed diam nonummy nibh euismod tincidunt ut laoreet dolore magna aliquam erat volutpat. Ut wisi enim ad minim veniam, quis nostrud exerci tation ullamcorper suscipit lobortis nisl ut aliquip ex ea commodo consequat.</p>
  </div>
  <div class="footer-line"></div><div class="page-no">07</div>
</section>

<!-- 08 Use cases -->
<section class="slide slide-sm" style="left:85px;top:961px">
  <div class="placeholder" role="img" aria-label="Faded background photo of stock market figures" style="left:0;top:0;width:288px;height:162px;background:linear-gradient(90deg,#e2e2e4,#f3f3f4 55%,#ffffff)"></div>
  <div class="brand"><span class="name">OBERI</span><span class="sub">Investment Group</span></div>
  <div class="phone" style="left:26px;top:21px;width:33px;height:72px"><p class="p-title">Lorem<br>ipsum dolor</p><div class="p-icon"></div><p class="p-copy">To introduce the students to the changing landscape of marketing and equip them with knowledge and tools to navigate the digital world</p></div>
  <div class="phone" style="left:68px;top:44px;width:33px;height:70px"><p class="p-title">Dolor sit<br>amet, conse</p><div class="p-icon"></div><p class="p-copy">You will learn concepts and ideas in digital marketing as well as how to use different tools and strategies to optimize your digital campaigns</p></div>
  <div class="phone" style="left:111px;top:66px;width:33px;height:71px"><p class="p-title">Consec<br>· · · · · ·</p><div class="p-icon"></div><p class="p-copy">You are required to pass 80% of this evaluation test to obtain the certificate. This evaluation test can only be taken 3 times.</p></div>
  <div class="abs h-light" style="left:161px;top:59px;font-size:15px;font-weight:300">USE CASES</div>
  <div class="abs copy" style="left:161px;top:83px;width:102px">
    <p>Lorem ipsum dolor sit amet, consectetuer adipiscing elit, sed diam nonummy nibh euismod tincidunt ut laoreet dolore magna aliquam erat volutpat. Ut wisi enim ad minim veniam, quis nostrud exerci tation ullamcorper suscipit lobortis nisl ut aliquip ex ea commodo consequat. Duis autem vel eum iriure dolor in hendrerit i</p><br>
    <p>Lorem ipsum dolor sit amet, consectetuer adipiscing elit, sed diam nonummy nibh euismod tincidunt ut laoreet dolore magna aliquam erat volutpat. Ut wisi enim ad minim veniam, quis nostrud exerci tation ullamcorper suscipit lobortis nisl ut aliquip ex ea commodo consequat. Duis autem vel eum iriure dolor in hendrerit in</p>
  </div>
  <div class="footer-line"></div><div class="page-no">08</div>
</section>

<!-- 09 Team -->
<section class="slide slide-sm" style="left:389px;top:961px">
  <div class="brand"><span class="name">OBERI</span><span class="sub">Investment Group</span></div>
  <div class="abs h-light" style="left:26px;top:19px;font-size:10px">TEAM MEMBERS<br><b style="font-weight:600">AND ADVISORS</b></div>
  <div class="abs" style="left:26px;top:44px;width:92px;height:1.5px;background:var(--rose)"></div>
  <div class="member" style="top:56px"><div class="avatar" role="img" aria-label="Portrait of team member"></div><p class="m-name">JONAS REED</p><p class="m-title">TITLE</p><p class="copy">A marketing strategy helps convey effective messages with the right level of marketing approaches that will maximise your sales outcome and marketing activities.</p></div>
  <div class="member" style="top:86px"><div class="avatar" role="img" aria-label="Portrait of team member"></div><p class="m-name">MILA HART</p><p class="m-title">TITLE</p><p class="copy">A marketing strategy helps convey effective messages with the right level of marketing approaches that will maximise your sales outcome and marketing activities.</p></div>
  <div class="member" style="top:116px"><div class="avatar" role="img" aria-label="Portrait of team member"></div><p class="m-name">ADA LOWE</p><p class="m-title">TITLE</p><p class="copy">A marketing strategy helps convey effective messages with the right level of marketing approaches that will maximise your sales outcome and marketing activities.</p></div>
  <svg class="abs" style="left:130px;top:35px" width="140" height="110" viewBox="130 35 140 110" role="img" aria-label="Team network with portrait nodes">
    <g stroke="var(--graphite)" stroke-width=".8">
      <line x1="203" y1="94" x2="230" y2="49"/><line x1="203" y1="94" x2="190" y2="59"/><line x1="203" y1="94" x2="241" y2="91"/>
      <line x1="203" y1="94" x2="181" y2="127"/><line x1="203" y1="94" x2="143" y2="100"/><line x1="241" y1="91" x2="253" y2="120"/>
    </g>
    <g fill="var(--rose-soft)"><circle cx="230" cy="49" r="10"/><circle cx="241" cy="91" r="10"/><circle cx="181" cy="127" r="10"/></g>
    <g fill="#c7c7c9"><circle cx="190" cy="59" r="10"/><circle cx="143" cy="100" r="10"/><circle cx="253" cy="120" r="10"/></g>
    <circle cx="203" cy="94" r="18" fill="var(--graphite)"/>
    <g font-size="6" fill="var(--ink)" font-family="Montserrat,sans-serif" font-weight="600"><text x="214" y="46">B</text><text x="200" y="72">A</text><text x="228" y="103">C</text><text x="258" y="107">D</text><text x="183" y="112">E</text><text x="155" y="119">F</text></g>
  </svg>
  <div class="footer-line"></div><div class="page-no">09</div>
</section>

<!-- Thank you -->
<section class="slide slide-sm thanks" style="left:692px;top:961px">
  <div class="placeholder" role="img" aria-label="Hand holding coins with a green seedling growing from them" style="left:140px;top:28px;width:148px;height:134px;background:radial-gradient(ellipse at 55% 45%,#5e8f3a 0 16%,#e9c3a8 38%,#ffffff 68%)"></div>
  <div class="brand"><span class="name">OBERI</span><span class="sub">Investment Group</span></div>
  <div class="abs h-rose" style="left:17px;top:79px;font-size:17px">Thank You</div>
  <div class="contact">
    <p>555-014-2290</p>
    <p>info@oberiinvestmentgroup.com</p>
    <p>www.oberiinvestmentgroup.com</p>
  </div>
</section>

</body>
</html>
```